Aid, Development & Consulting Firm

Harwell Bracegirdle Consulting Pty Ltd is a small firm in Australia whose principal works in the area of aid and development. His experience is broad ranging from aid project design and evaluation; to offering security advice in running aid operations in dangerous situations. He works with governments and private firms in conducting training for personnel travelling to work in dangerous or difficult regions. He has worked for many years with NGO's (aid organisations) and consults to the WCF. He works in locations all over the globe which include trouble spots like Iraq and Sudan, to sleepier locales like Samoa and Fiji. Being on Asia's doorstep much time is spent in Asia eg Indonesia, Vietnam. He is often called on to monitor and evaluate aid projects throughtout the globe.

Target Market(s)

Government Aid Divisions eg in Oz, FendCor; WCF; NGO's and consulting firms who work in developing countries

Industry/Entity Type

Security

Requirements
Nice to have
• Try and incorporate a global feel without being obvious i.e. no starving children as the primary work done is a step beyond obvious aid relief. Something very simple but bold and stylish as card holder is not a "touchy" feely person
Should not have
• No starving kid type scenarios. Prefer no pictures

```html
<!DOCTYPE html>
<html lang="en">
<head>
<meta charset="utf-8">
<title>Harwell Bracegirdle Consulting – Business Card</title>
<link rel="stylesheet" href="https://fonts.googleapis.com/css2?family=PT+Sans+Narrow&family=Michroma&family=Archivo:wght@700&family=Arimo&display=swap">
<style>
  :root {
    --backdrop: #ececec;
    --card-white: #ffffff;
    --card-blue: #009fdf;
    --ink-navy: #24477c;
    --ink-red: #8e2a2b;
    --mark-blue: #2d9ad6;
    --halo-light: #c9e0f3;
    --halo-dark: #1f5a95;
    --icon-navy: #1b4f86;
    --text-white: #ffffff;
  }
  * { margin: 0; padding: 0; box-sizing: border-box; }
  html, body { width: 1200px; height: 900px; overflow: hidden; }
  body { background: var(--backdrop); position: relative; font-family: "Arimo", Arial, sans-serif; }

  .card { position: absolute; left: 282px; width: 636px; height: 388px; overflow: hidden; }
  .card--front { top: 44px; background: var(--card-white); }
  .card--back { top: 470px; background: var(--card-blue); }

  .halo { position: absolute; border-radius: 50%; }
  .card--front .halo { left: 350px; top: 120px; width: 320px; height: 320px; background: var(--halo-light); opacity: .8; filter: blur(2px); }
  .card--back .halo { left: 358px; top: 118px; width: 300px; height: 300px; background: var(--halo-dark); opacity: .85; filter: blur(3px); }

  .brand-dot { position: absolute; left: 270px; top: 20px; width: 96px; height: 96px; border-radius: 50%; background: var(--mark-blue); }

  .company-name { position: absolute; left: 0; right: 0; top: 118px; text-align: center;
    font-family: "PT Sans Narrow", "Arial Narrow", sans-serif; font-size: 35px; color: var(--ink-navy); line-height: 1; }

  .services { position: absolute; left: 0; right: 0; top: 165px; text-align: center;
    font-family: "Michroma", sans-serif; font-size: 13px; letter-spacing: 2.5px; color: var(--ink-red); line-height: 1; }
  .services .divider { margin: 0 22px; font-family: "Arimo", sans-serif; font-size: 18px; vertical-align: -2px; }

  .holder-name { position: absolute; left: 0; right: 0; top: 242px; text-align: center;
    font-family: "Archivo", Arial, sans-serif; font-weight: 700; font-size: 22px; letter-spacing: 1px; color: var(--ink-navy); line-height: 1; }
  .holder-role { position: absolute; left: 246px; top: 270px;
    font-family: "Michroma", sans-serif; font-size: 15px; letter-spacing: 2px; color: var(--ink-red); line-height: 1; font-variant: small-caps; }

  .contact { position: absolute; left: 52px; color: var(--text-white); font-size: 18px; line-height: 27.5px; }
  .contact--address { top: 126px; }
  .contact--lines { top: 236px; }
  .contact-row { display: flex; align-items: center; }
  .contact-icon { width: 22px; height: 22px; margin-right: 18px; flex: none; fill: var(--icon-navy); stroke: var(--icon-navy); }
  .address-block { display: flex; }
  .address-block .contact-icon { margin-top: 4px; }
</style>
</head>
<body>
  <section class="card card--front">
    <div class="halo" role="img" aria-label="Soft decorative circle"></div>
    <div class="brand-dot"></div>
    <h1 class="company-name">Harwell Bracegirdle Consulting Pty Ltd</h1>
    <p class="services">AID<span class="divider">|</span>DEVELOPMENT<span class="divider">|</span>CONSULTING</p>
    <p class="holder-name">B. Harwell Bracegirdle</p>
    <p class="holder-role">Director</p>
  </section>

  <section class="card card--back">
    <div class="halo" role="img" aria-label="Soft decorative circle"></div>

    <div class="contact contact--address address-block">
      <svg class="contact-icon" viewBox="0 0 22 22" stroke="none"><path d="M11 1a7 7 0 0 0-7 7c0 5 7 13 7 13s7-8 7-13a7 7 0 0 0-7-7z"/></svg>
      <address style="font-style:normal">42 Wattle Crescent<br>Linden Vale<br>SA 5099 Australia</address>
    </div>

    <div class="contact contact--lines">
      <div class="contact-row">
        <svg class="contact-icon" viewBox="0 0 22 22" stroke="none"><path d="M2 7c2-4 16-4 18 0v2h-5V7H7v2H2z"/><path d="M5 11h12l3 8H2z"/><circle cx="11" cy="15" r="2.2" fill="#009fdf"/></svg>
        <span>+61 8 5550 1234</span>
      </div>
      <div class="contact-row">
        <svg class="contact-icon" viewBox="0 0 22 22" fill="none" stroke-width="1.6"><rect x="6" y="1.5" width="10" height="19" rx="1.5"/><line x1="6" y1="4.5" x2="16" y2="4.5"/><line x1="6" y1="17" x2="16" y2="17"/></svg>
        <span>+61 (0) 4000 55512</span>
      </div>
      <div class="contact-row">
        <svg class="contact-icon" viewBox="0 0 22 22" fill="none" stroke-width="1.6"><rect x="1.5" y="5" width="19" height="13"/><path d="M1.5 5l9.5 8 9.5-8M1.5 18l7-6.5M20.5 18l-7-6.5"/></svg>
        <span>harwell@mailpoint.com</span>
      </div>
      <div class="contact-row">
        <svg class="contact-icon" viewBox="0 0 22 22" fill="none" stroke-width="1.6"><rect x="1.5" y="5" width="19" height="13"/><path d="M1.5 5l9.5 8 9.5-8M1.5 18l7-6.5M20.5 18l-7-6.5"/></svg>
        <span>harwellb@postbox.com</span>
      </div>
    </div>
  </section>
</body>
</html>
```